Business Card for Industrial Distributor

We need a business card design for an industrial distributor. We sell machine parts for the manufacturing and oil industry. We would like the cards to look clean and modern but with a touch of industry.

Our colors are blue/white.

Please feel free to visit our website www.krovelmint.com

Target Market(s)

mexican manufacturers in the automobile/aerospace industry

Industry/Entity Type

Industrial

Colors
ffffff
0555a3

```html
<!DOCTYPE html>
<html lang="en">
<head>
<meta charset="utf-8">
<title>Krovelmint Business Card</title>
<link rel="stylesheet" href="https://fonts.googleapis.com/css2?family=Montserrat:wght@400;500;700&display=swap">
<style>
  :root {
    --stage: #d1d2d4;
    --stage-border: #8a8b8d;
    --card-white: #ffffff;
    --navy: #2b3590;
    --brand-blue: #0555a3;
    --accent-blue: #1f73c0;
    --back-center: #1b73c4;
    --back-edge: #283593;
    --shadow: rgba(0, 0, 0, 0.45);
  }
  html, body {
    margin: 0;
    padding: 0;
    width: 1200px;
    height: 928px;
    overflow: hidden;
  }
  body {
    font-family: "Montserrat", sans-serif;
  }
  .stage {
    position: relative;
    width: 1200px;
    height: 928px;
    box-sizing: border-box;
    background: var(--stage);
    border: 2px solid var(--stage-border);
  }
  .card {
    position: absolute;
    top: 98px;
    width: 417px;
    height: 730px;
    border-radius: 36px;
    box-shadow: 8px 10px 12px var(--shadow);
    overflow: hidden;
  }
  .card-front {
    left: 168px;
    background: var(--card-white);
  }
  .card-back {
    left: 615px;
    background: radial-gradient(circle at 54% 48%, var(--back-center) 0%, #1d5fb2 45%, var(--back-edge) 100%);
  }
  .brand {
    position: absolute;
    left: 28px;
    top: 60px;
    display: flex;
    align-items: center;
    gap: 12px;
  }
  .brand-dot {
    width: 58px;
    height: 58px;
    border-radius: 50%;
    background: var(--brand-blue);
  }
  .brand-name {
    font-weight: 700;
    font-size: 46px;
    color: var(--navy);
    letter-spacing: -0.5px;
  }
  .rule {
    position: absolute;
    left: 83px;
    width: 252px;
    height: 3px;
    background: linear-gradient(90deg, rgba(31,115,192,0) 0%, var(--accent-blue) 25%, var(--navy) 75%, rgba(43,53,144,0) 100%);
  }
  .rule-top { top: 423px; }
  .rule-bottom { top: 676px; }
  .contact {
    position: absolute;
    left: 0;
    width: 100%;
    top: 440px;
    text-align: center;
    color: var(--navy);
  }
  .person-name {
    margin: 0;
    font-size: 27px;
    font-weight: 500;
    line-height: 34px;
  }
  .person-role {
    margin: 0;
    font-size: 17px;
    color: var(--accent-blue);
    line-height: 24px;
  }
  .address {
    margin: 10px 0 0;
    font-size: 17px;
    font-style: normal;
    line-height: 23px;
  }
  .icon-row {
    display: flex;
    justify-content: center;
    gap: 4px;
    margin-top: 12px;
    height: 14px;
  }
  .icon-row svg {
    width: 13px;
    height: 13px;
  }
  .details {
    margin: 17px 0 0;
    padding: 0;
    list-style: none;
    font-size: 17px;
    line-height: 23px;
  }
  .details .web { color: var(--accent-blue); }
  .details .web span { color: var(--navy); }
  .back-disc {
    position: absolute;
    left: 103px;
    top: 228px;
    width: 248px;
    height: 248px;
    border-radius: 50%;
    background: var(--card-white);
  }
</style>
</head>
<body>
<main class="stage">
  <section class="card card-front">
    <div class="brand">
      <div class="brand-dot"></div>
      <div class="brand-name">Krovelmint</div>
    </div>

    <div class="rule rule-top"></div>

    <div class="contact">
      <h1 class="person-name">Marlo Pennick</h1>
      <p class="person-role">Director</p>
      <address class="address">P.O. Box 4417<br>Fernwood, M I 49622</address>

      <div class="icon-row" aria-hidden="true">
        <svg viewBox="0 0 16 16"><path fill="#1f73c0" d="M3.5 1.5l2.5 0 1 3.5-1.7 1.2c.8 1.8 2.2 3.3 4 4.1l1.3-1.7 3.4 1v2.6c0 .8-.7 1.4-1.5 1.3C6.8 13 3 9.2 2.2 3c-.1-.8.5-1.5 1.3-1.5z"/></svg>
        <svg viewBox="0 0 16 16"><rect x="1.5" y="3.5" width="13" height="9" rx="1" fill="none" stroke="#1f73c0" stroke-width="1.6"/><path d="M2 4.2l6 4.6 6-4.6" fill="none" stroke="#1f73c0" stroke-width="1.6"/></svg>
        <svg viewBox="0 0 16 16"><circle cx="8" cy="8" r="6.5" fill="none" stroke="#1f73c0" stroke-width="1.4"/><ellipse cx="8" cy="8" rx="2.8" ry="6.5" fill="none" stroke="#1f73c0" stroke-width="1.2"/><path d="M1.5 8h13M2.6 4.8h10.8M2.6 11.2h10.8" stroke="#1f73c0" stroke-width="1.1"/></svg>
      </div>

      <ul class="details">
        <li>+330 5182-0943</li>
        <li>info@krovelmint.com</li>
        <li class="web"><span>www.</span>krovelmint<span>.com</span></li>
      </ul>
    </div>

    <div class="rule rule-bottom"></div>
  </section>

  <section class="card card-back">
    <div class="back-disc"></div>
  </section>
</main>
</body>
</html>
```